Business Card Design

Marla Quenby
Artist of Contemporary/Modern/Representational Art
Contact: 0429175348
Please include my web site (thanks)! http://www.artloft583.com.au/marla-quenby
And
Email: marlaquenby@vexmail.com

Target Market(s)

Modern professional People who know what they like in modern contemporary art and have the means to purchase it.

Industry/Entity Type

Business

Contact Information for Business Card

Marla Quenby
Contact: 0429175348

Font styles to use
Sans Serif

Requirements
Must have
• Simplicity & to the point
Keep the font modern/ contemporary
Nice to have
• A portrait of me and one piece of work on the business card (one on each side).
Should not have
• I'm not into butterflies.
No feminine style swirls
Nor I like swirls that look like tatoos

```html
<!DOCTYPE html>
<html lang="en">
<head>
<meta charset="utf-8">
<title>Marla Quenby — Business Card</title>
<link rel="stylesheet" href="https://fonts.googleapis.com/css2?family=Arimo:wght@400;700&display=swap">
<style>
  :root {
    --page: #ffffff;
    --card-dark: #2a2d2b;
    --card-dark-edge: #232624;
    --olive: #c3bd5b;
    --white: #ffffff;
    --art-left-top: #3f6f8f;
    --art-left-mid: #d8a23a;
    --art-left-low: #b2453a;
    --art-right-top: #9fb7b3;
    --art-right-mid: #c76b45;
    --art-right-low: #5d6a58;
  }
  * { margin: 0; padding: 0; box-sizing: border-box; }
  html, body {
    width: 900px; height: 1200px; overflow: hidden;
    background: var(--page);
    font-family: "Arimo", Arial, sans-serif;
  }
  .canvas { position: relative; width: 900px; height: 1200px; }

  .card-front {
    position: absolute; left: 106px; top: 114px; width: 707px; height: 434px;
    background:
      radial-gradient(ellipse at 30% 20%, rgba(255,255,255,0.04), transparent 60%),
      linear-gradient(160deg, var(--card-dark), var(--card-dark-edge));
    overflow: hidden;
  }
  .portrait {
    position: absolute; left: 87px; top: 64px; width: 126px; height: 154px;
    border: 2px solid var(--olive);
    background: radial-gradient(circle at 50% 45%, #c79a86 0%, #6b4a3a 45%, #3c4a30 100%);
  }
  .accent-bar {
    position: absolute; left: 87px; top: 231px; width: 126px; height: 203px;
    background: var(--olive);
  }
  .identity { position: absolute; left: 268px; top: 151px; }
  .identity .name {
    color: var(--white); font-weight: 700; font-size: 19px; line-height: 24px;
  }
  .identity .role {
    color: var(--olive); font-weight: 400; font-size: 20.5px; line-height: 25px;
  }
  .contacts { position: absolute; left: 270px; top: 290px; list-style: none; }
  .contacts li {
    display: flex; align-items: center; gap: 13px;
    color: var(--white); font-size: 18.5px; line-height: 24px; white-space: nowrap;
  }
  .contacts svg { width: 16px; height: 16px; flex: none; }

  .card-back {
    position: absolute; left: 106px; top: 679px; width: 707px; height: 434px;
    display: flex; background: var(--olive);
  }
  .artwork { height: 100%; }
  .artwork--left {
    width: 352px;
    background: linear-gradient(180deg, var(--art-left-top) 0%, var(--art-left-mid) 30%, var(--art-left-low) 65%, #c9a2a8 100%);
  }
  .artwork--right {
    width: 350px; margin-left: 5px;
    background: linear-gradient(180deg, var(--art-right-top) 0%, var(--art-right-mid) 45%, var(--art-right-low) 100%);
  }
</style>
</head>
<body>
<div class="canvas">
  <section class="card-front">
    <div class="portrait" role="img" aria-label="Portrait photograph of the artist"></div>
    <div class="accent-bar"></div>
    <div class="identity">
      <p class="name">Marla QUENBY</p>
      <p class="role">Artist of Contemporary</p>
      <p class="role">Modern | Representational Art</p>
    </div>
    <ul class="contacts">
      <li>
        <svg viewBox="0 0 16 16" fill="none" stroke="var(--olive)" stroke-width="1.1"><rect x="1.5" y="3.5" width="13" height="9"/><path d="M1.5 3.5 8 9l6.5-5.5M1.5 12.5l5-4.5M14.5 12.5l-5-4.5"/></svg>
        marlaquenby@vexmail.com
      </li>
      <li>
        <svg viewBox="0 0 16 16" fill="none" stroke="var(--olive)" stroke-width="1.1"><path d="M3.5 1.5l2.5 2.5-1.5 2a8 8 0 0 0 5.5 5.5l2-1.5 2.5 2.5-2 2C7 14 2 9 1.5 3.5z"/></svg>
        0429175348
      </li>
      <li>
        <svg viewBox="0 0 16 16" fill="none" stroke="var(--olive)" stroke-width="1.1"><circle cx="8" cy="8" r="6.5"/><ellipse cx="8" cy="8" rx="3" ry="6.5"/><path d="M1.5 8h13M2.5 4.8h11M2.5 11.2h11"/></svg>
        www.artloft583.com.au/marla-quenby
      </li>
    </ul>
  </section>

  <section class="card-back">
    <div class="artwork artwork--left" role="img" aria-label="Painting of a row of tall colourful gabled townhouses above blossoming trees"></div>
    <div class="artwork artwork--right" role="img" aria-label="Painting of an old town island with church spires and colourful rooftops by the water"></div>
  </section>
</div>
</body>
</html>
```